Business cards and logo for a international shipping company called Meridane Freight LLC. We would like to incorporate the colors red and blue. We would like the theme to be nautical.

Industry/Entity Type

Business

```html
<!DOCTYPE html>
<html lang="en">
<head>
<meta charset="UTF-8">
<title>Meridane Freight LLC — Business Cards</title>
<link href="https://fonts.googleapis.com/css2?family=Open+Sans:wght@400;600;800&display=swap" rel="stylesheet">
<style>
  :root {
    --page-bg: #e4e5e7;
    --card-white: #f7f7f5;
    --brand-blue: #1a8fcd;
    --brand-red: #c8161d;
    --ink: #1c1c1c;
    --white: #ffffff;
  }
  * { margin: 0; padding: 0; box-sizing: border-box; }
  html, body {
    width: 1200px; height: 1200px; overflow: hidden;
    background: var(--page-bg);
    font-family: "Open Sans", Arial, sans-serif;
  }
  .sheet {
    width: 1200px; height: 1200px;
    display: flex; flex-direction: column; align-items: center; justify-content: center;
    gap: 60px;
  }
  .card {
    position: relative;
    width: 840px; height: 480px;
    overflow: hidden;
    box-shadow: 0 6px 18px rgba(0,0,0,0.18);
  }
  /* Front */
  .card--front { background: var(--brand-blue); }
  .card--front .wordmark {
    position: absolute; right: 90px; top: 150px;
    text-align: right;
    color: var(--white);
    font-weight: 800;
    line-height: 1.05;
  }
  .wordmark__line1 { display: block; font-size: 84px; letter-spacing: 1px; }
  .wordmark__line2 { display: block; font-size: 46px; letter-spacing: 4px; }
  .card--front .web {
    position: absolute; left: 90px; bottom: 70px;
    color: var(--white);
    font-size: 24px; letter-spacing: 11px;
  }
  /* Back */
  .card--back { background: var(--card-white); }
  .contact {
    position: absolute; left: 70px; top: 80px;
    color: var(--ink);
  }
  .contact__name { font-size: 32px; font-weight: 600; }
  .contact__title { font-size: 18px; margin: 0 0 22px 2px; }
  .contact__rows { font-size: 19px; line-height: 1.45; }
  .contact__row { display: flex; }
  .contact__label { width: 34px; }
  .card--back .wordmark {
    position: absolute; right: 60px; top: 80px;
    text-align: right;
    color: var(--brand-red);
    font-weight: 800;
    line-height: 1.05;
  }
  .card--back .wordmark__line1 { font-size: 56px; }
  .card--back .wordmark__line2 { font-size: 30px; letter-spacing: 3px; }
  .wave-band { position: absolute; left: 0; bottom: 0; width: 840px; height: 170px; }
</style>
</head>
<body>
  <main class="sheet">
    <section class="card card--front" aria-label="Card front">
      <div class="wordmark">
        <span class="wordmark__line1">MERIDANE</span>
        <span class="wordmark__line2">FREIGHT LLC</span>
      </div>
      <p class="web">www.meridanefreight.com</p>
    </section>

    <section class="card card--back" aria-label="Card back">
      <div class="contact">
        <p class="contact__name">Your Full Name</p>
        <p class="contact__title">Your Tittle</p>
        <div class="contact__rows">
          <div class="contact__row"><span class="contact__label">A</span><span>: Your address line 1<br>&nbsp;&nbsp;Your address line 2</span></div>
          <div class="contact__row"><span class="contact__label">P</span><span>: 012.345.6789</span></div>
          <div class="contact__row"><span class="contact__label">E</span><span>: Your email@meridanefreight.com</span></div>
          <div class="contact__row"><span class="contact__label">W</span><span>: www.meridanefreight.com</span></div>
        </div>
      </div>
      <div class="wordmark">
        <span class="wordmark__line1">MERIDANE</span>
        <span class="wordmark__line2">FREIGHT LLC</span>
      </div>
      <svg class="wave-band" viewBox="0 0 840 170" preserveAspectRatio="none" aria-hidden="true">
        <path d="M0 50 C 250 60, 500 110, 840 110 L 840 170 L 0 170 Z" fill="var(--brand-blue)"/>
        <path d="M80 60 C 260 80, 420 110, 560 128 C 400 112, 240 86, 80 60 Z" fill="var(--brand-red)" stroke="var(--brand-red)" stroke-width="6" stroke-linejoin="round"/>
      </svg>
    </section>
  </main>
</body>
</html>
```